ROVA NET LTD

Advertisement to get more schools:
use website https://www.rova-net.co.uk for logos etc.
ICT Service Level Agreements for as little as £2000 per year
Unlimited Remote, phone and email support
Unlimited Call outs included
90% fix time within 30 minutes of ticket submission
Extra support during Brelcom inspections
GDPR service included

Education

```html
<!DOCTYPE html>
<html lang="en">
<head>
<meta charset="utf-8">
<title>Rova Net – ICT Support for Schools</title>
<link href="https://fonts.googleapis.com/css2?family=Arimo:wght@700&family=Roboto:wght@400;500;700&display=swap" rel="stylesheet">
<style>
  :root {
    --blue: #0f6cb6;
    --blue-deep: #0a63ad;
    --orange: #f47f4a;
    --ink: #1f1f1f;
    --paper: #ffffff;
    --paper-soft: #f5f7fa;
    --rule: rgba(255,255,255,0.35);
  }
  * { box-sizing: border-box; margin: 0; padding: 0; }
  html, body { width: 1200px; height: 2403px; overflow: hidden; }
  body { font-family: "Roboto", sans-serif; background: var(--paper); position: relative; }

  .top-bar { position: absolute; left: 0; top: 0; width: 1200px; height: 9px; background: var(--blue); }

  .brand { position: absolute; left: 0; width: 1200px; text-align: center; font-family: "Roboto", sans-serif; font-weight: 700; letter-spacing: 4px; }
  .brand--header { top: 36px; font-size: 52px; color: var(--blue); }
  .brand--footer { top: 2040px; font-size: 64px; color: var(--paper); }

  .hero-frame { position: absolute; left: 0; top: 136px; width: 1200px; height: 737px; background: var(--orange); border-radius: 60px 0 60px 60px; }
  .hero-photo { position: absolute; left: 0; top: 136px; width: 1182px; height: 719px; border-radius: 60px 0 48px 60px;
    background: linear-gradient(120deg, #6d4a3e 0%, #a98f7d 35%, #c9b98a 55%, #8c9aa8 80%, #d5d8dc 100%); }
  .hero-title { position: absolute; left: 231px; top: 411px; width: 684px; height: 170px; background: rgba(70,60,55,0.72);
    color: var(--paper); font-family: "Arimo", sans-serif; font-weight: 700; font-size: 51px; line-height: 64px;
    text-align: center; display: flex; align-items: center; justify-content: center; }

  .features-bg { position: absolute; left: 0; top: 873px; width: 1200px; height: 1100px; background: var(--paper-soft); }
  .student-photo { position: absolute; left: 630px; top: 960px; width: 570px; height: 1010px;
    border-radius: 280px 0 0 0;
    background: linear-gradient(180deg, #4a3428 0%, #b98563 22%, #f3efe9 45%, #8aa6c6 70%, #5e7ea6 100%); }

  .feature-list { position: absolute; left: 108px; top: 995px; list-style: none; }
  .feature { position: absolute; left: 0; width: 560px; height: 118px; display: flex; align-items: center; }
  .feature-icon { width: 130px; height: 118px; border-radius: 40px 0 0 40px; display: flex; align-items: center; justify-content: center; flex: none; }
  .feature-icon--blue { background: var(--blue); }
  .feature-icon--orange { background: var(--orange); }
  .feature-text { margin-left: 32px; font-size: 26px; font-weight: 500; line-height: 45px; color: var(--ink); }

  .footer-frame { position: absolute; left: 0; top: 1968px; width: 1200px; height: 435px; background: var(--orange); border-radius: 66px 66px 0 0; }
  .footer { position: absolute; left: 14px; top: 1983px; width: 1186px; height: 420px; background: var(--blue-deep); border-radius: 60px 60px 0 0; }

  .contact { position: absolute; top: 2194px; display: flex; align-items: center; color: var(--paper); }
  .contact-badge { width: 64px; height: 64px; border-radius: 50%; background: var(--paper); display: flex; align-items: center; justify-content: center; flex: none; }
  .contact-body { margin-left: 22px; }
  .contact-label { font-size: 24px; font-weight: 700; line-height: 30px; }
  .contact-value { font-size: 22px; line-height: 32px; }

  .footer-rule { position: absolute; left: 140px; top: 2295px; width: 920px; height: 1px; background: var(--rule); }
  .social { position: absolute; top: 2330px; width: 40px; height: 40px; border: 2px solid var(--paper); border-radius: 50%; }
  .copyright { position: absolute; left: 0; width: 1200px; top: 2336px; text-align: center; font-size: 22px; color: var(--paper); }
  .ref-code { position: absolute; left: 1143px; top: 2354px; font-size: 19px; color: var(--paper); }
</style>
</head>
<body>
  <div class="top-bar"></div>
  <div class="brand brand--header">ROVA NET</div>

  <div class="hero-frame"></div>
  <div class="hero-photo" role="img" aria-label="Pupil wearing a VR headset in a classroom with classmates behind"></div>
  <h1 class="hero-title">Education, Support and<br>Installation of All</h1>

  <div class="features-bg"></div>
  <div class="student-photo" role="img" aria-label="Smiling schoolgirl holding a tablet"></div>

  <ul class="feature-list">
    <li class="feature" style="top:0">
      <div class="feature-icon feature-icon--blue">
        <svg width="66" height="66" viewBox="0 0 66 66" fill="none" stroke="#fff" stroke-width="3" stroke-linejoin="round" stroke-linecap="round"><path d="M6 30l12-12 10 6 8-4 12 2 12 10-14 16-10-8"/><path d="M18 34l8 8m-2-14l12 12m-4-16l12 12"/><path d="M33 4v8M22 8l4 6M44 8l-4 6"/></svg>
      </div>
      <p class="feature-text">ICT SLA agreements for as little<br>as £2000 per year</p>
    </li>
    <li class="feature" style="top:148px">
      <div class="feature-icon feature-icon--orange">
        <svg width="66" height="66" viewBox="0 0 66 66" fill="none" stroke="#fff" stroke-width="3" stroke-linecap="round"><circle cx="30" cy="30" r="9"/><path d="M16 54c2-10 8-14 14-14s12 4 14 14"/><path d="M16 30a14 14 0 0 1 28 0"/><rect x="44" y="6" width="18" height="12" rx="2"/><path d="M8 22a24 24 0 0 1 6-10M52 40a24 24 0 0 1-6 10"/></svg>
      </div>
      <p class="feature-text">Unlimited Remote, phone and<br>email support</p>
    </li>
    <li class="feature" style="top:298px">
      <div class="feature-icon feature-icon--blue">
        <svg width="66" height="66" viewBox="0 0 66 66" fill="none" stroke="#fff" stroke-width="3" stroke-linejoin="round" stroke-linecap="round"><path d="M12 14l8-4 6 12-5 4c3 7 8 12 15 15l4-5 12 6-4 8c-20-2-34-16-36-36z"/><rect x="36" y="8" width="22" height="22" rx="3"/><circle cx="47" cy="16" r="3"/><path d="M41 26c1-4 11-4 12 0"/></svg>
      </div>
      <p class="feature-text">Unlimited Call outs included</p>
    </li>
    <li class="feature" style="top:447px">
      <div class="feature-icon feature-icon--orange">
        <svg width="66" height="66" viewBox="0 0 66 66" fill="none" stroke="#fff" stroke-width="3" stroke-linejoin="round"><path d="M10 18l28-8 6 20a5 5 0 0 0 0 8l4 14-28 8-4-14a5 5 0 0 0 0-8z"/><path d="M22 22l4 14m6-16l4 14m-10 8l12-4"/></svg>
      </div>
      <p class="feature-text">90% fix time within 30 minutes<br>of ticket submission</p>
    </li>
    <li class="feature" style="top:597px">
      <div class="feature-icon feature-icon--blue">
        <svg width="66" height="66" viewBox="0 0 66 66" fill="none" stroke="#fff" stroke-width="3" stroke-linejoin="round" stroke-linecap="round"><rect x="10" y="10" width="36" height="48" rx="3"/><rect x="20" y="6" width="16" height="8" rx="2"/><path d="M16 24l3 3 5-5M16 36l3 3 5-5M16 48l3 3 5-5M30 26h10M30 38h8"/><path d="M58 20L38 52l-4 4 1-6 20-32z"/></svg>
      </div>
      <p class="feature-text">Extra support during Brelcom<br>inspections</p>
    </li>
    <li class="feature" style="top:745px">
      <div class="feature-icon feature-icon--orange">
        <svg width="66" height="66" viewBox="0 0 66 66" fill="none" stroke="#fff" stroke-width="3" stroke-linejoin="round" stroke-linecap="round"><rect x="8" y="6" width="40" height="50" rx="3"/><path d="M14 16h28"/><rect x="18" y="34" width="18" height="14" rx="2"/><path d="M22 34v-5a5 5 0 0 1 10 0v5"/><path d="M50 38l10 4v8c0 6-5 9-10 11-5-2-10-5-10-11v-8z"/><path d="M46 50l3 3 6-6"/></svg>
      </div>
      <p class="feature-text">GDPR service included</p>
    </li>
  </ul>

  <div class="footer-frame"></div>
  <div class="footer"></div>
  <div class="brand brand--footer">ROVA NET</div>

  <div class="contact" style="left:124px">
    <div class="contact-badge">
      <svg width="26" height="26" viewBox="0 0 24 24" fill="none" stroke="#f47f4a" stroke-width="2"><circle cx="12" cy="12" r="10"/><path d="M2 12h20M12 2c3 3 4 7 4 10s-1 7-4 10c-3-3-4-7-4-10s1-7 4-10z"/></svg>
    </div>
    <div class="contact-body">
      <p class="contact-label">Website</p>
      <p class="contact-value">www.rova-net.co.uk/</p>
    </div>
  </div>
  <div class="contact" style="left:482px">
    <div class="contact-badge">
      <svg width="24" height="24" viewBox="0 0 24 24"><path fill="#f47f4a" d="M6.6 10.8a15 15 0 0 0 6.6 6.6l2.2-2.2a1 1 0 0 1 1-.25 11.4 11.4 0 0 0 3.6.57 1 1 0 0 1 1 1V20a1 1 0 0 1-1 1A17 17 0 0 1 3 4a1 1 0 0 1 1-1h3.5a1 1 0 0 1 1 1c0 1.25.2 2.45.57 3.57a1 1 0 0 1-.25 1z"/></svg>
    </div>
    <div class="contact-body">
      <p class="contact-label">Phone</p>
      <p class="contact-value">0161 555 0142</p>
    </div>
  </div>
  <div class="contact" style="left:791px">
    <div class="contact-badge">
      <svg width="24" height="24" viewBox="0 0 24 24"><path fill="#f47f4a" d="M2 6a2 2 0 0 1 2-2h16a2 2 0 0 1 2 2v.4l-10 6-10-6zM2 8.7l10 6 10-6V18a2 2 0 0 1-2 2H4a2 2 0 0 1-2-2z"/></svg>
    </div>
    <div class="contact-body">
      <p class="contact-label">Email</p>
      <p class="contact-value">info@rova-net.co.uk</p>
    </div>
  </div>

  <div class="footer-rule"></div>
  <div class="social" style="left:154px"></div>
  <div class="social" style="left:204px"></div>
  <p class="copyright">Copyright © 2022 Rova Net &nbsp;|&nbsp; All Rights Reserved</p>
  <p class="ref-code">C37</p>
</body>
</html>
```